Gourmet cookie company needs a label designed

We need a label designed for a new cookie company. We make mini cookies. The labels will be placed on either white tins or clear containers. We would like some bright and eye catching label although not child like. Our target customer is adults not kids.
Any color/colors acceptable. The initial label will be a square 4" label but the design should also be able to be formatted to fit on a round label as well in the future.

Text on label: Rosalind's Wafer Crumb Company; Chocolate Chip; All Natural; New Wt. 8.0oz

```html
<!DOCTYPE html>
<html lang="en">
<head>
<meta charset="utf-8">
<title>Rosalind's Wafer Crumb Company – Chocolate Chip Label</title>
<link rel="stylesheet" href="https://fonts.googleapis.com/css2?family=Yellowtail&family=Montserrat:wght@400;500&display=swap">
<style>
  :root {
    --backdrop-light: #ffffff;
    --backdrop-dark: #d6d6d6;
    --label-orange: #f1a153;
    --ribbon-peach: #f8c598;
    --ribbon-fold: #ee7f22;
    --label-white: #ffffff;
  }
  html, body {
    margin: 0;
    padding: 0;
    width: 1200px;
    height: 900px;
    overflow: hidden;
  }
  body {
    background: radial-gradient(ellipse 70% 75% at 50% 50%, var(--backdrop-light) 20%, var(--backdrop-dark) 100%);
  }
  .label {
    display: block;
    width: 1200px;
    height: 900px;
  }
  .brand-name {
    font-family: "Yellowtail", cursive;
    font-size: 84px;
    fill: var(--label-orange);
  }
  .brand-tagline {
    font-family: "Montserrat", sans-serif;
    font-weight: 500;
    font-size: 10px;
    letter-spacing: 3.2px;
    fill: var(--label-orange);
  }
  .flavour {
    font-family: "Montserrat", sans-serif;
    font-weight: 400;
    font-size: 19px;
    letter-spacing: 4.5px;
    fill: var(--label-white);
  }
  .claim {
    font-family: "Montserrat", sans-serif;
    font-weight: 500;
    font-size: 11.5px;
    letter-spacing: 2.4px;
    fill: var(--label-orange);
  }
  .net-weight {
    font-family: "Montserrat", sans-serif;
    font-weight: 500;
    font-size: 9px;
    letter-spacing: 1.6px;
    fill: var(--label-orange);
  }
</style>
</head>
<body>
<svg class="label" viewBox="0 0 1200 900" xmlns="http://www.w3.org/2000/svg">
  <g class="seal">
    <circle class="seal-outer" cx="600" cy="450" r="268" fill="var(--label-orange)"/>
    <circle class="seal-rule" cx="600" cy="450" r="201" fill="none" stroke="var(--label-white)" stroke-width="1.2"/>
    <circle class="seal-face" cx="600" cy="450" r="182" fill="var(--label-white)"/>
  </g>

  <g class="brand">
    <text class="brand-name" x="608" y="440" text-anchor="middle">Rosalind's</text>
    <text class="brand-tagline" x="638" y="464" text-anchor="middle">WAFER CRUMB COMPANY</text>
  </g>

  <g class="ribbon">
    <polygon class="ribbon-tail" points="362,508 408,508 408,562 362,562 380,535" fill="var(--ribbon-peach)"/>
    <polygon class="ribbon-tail" points="838,508 792,508 792,562 838,562 820,535" fill="var(--ribbon-peach)"/>
    <polygon class="ribbon-fold" points="388,545 408,545 408,562" fill="var(--ribbon-fold)"/>
    <polygon class="ribbon-fold" points="812,545 792,545 792,562" fill="var(--ribbon-fold)"/>
    <rect class="ribbon-band" x="388" y="490" width="424" height="55" fill="var(--ribbon-peach)"/>
    <text class="flavour" x="602" y="524" text-anchor="middle">CHOCOLATE CHIP</text>
  </g>

  <g class="details">
    <text class="claim" x="601" y="577" text-anchor="middle">ALL NATURAL</text>
    <text class="net-weight" x="601" y="595" text-anchor="middle">NET WT 8oz</text>
  </g>
</svg>
</body>
</html>
```